TEK Logistics - Banner 2.5' x 8' for 20+ locations

Need a banner designed that will pop. This banner will be displayed at over 20 of our transportation facilities. Goal is for the banner to grab the attention of employees, contractors and clients and help reinforce our mission and core values. Designed needs to include TEK Logo, our core values and mission statement. Red and Black are the main company colors and we need to stay within that theme and color pallet. Attached is a previous version that was too basic and boring. Willing to consider a design that excludes the mission statement.

Gathering more feedback

```html
<!DOCTYPE html>
<html lang="en">
<head>
<meta charset="utf-8">
<title>TEK Logistics – Core Values Banner</title>
<link href="https://fonts.googleapis.com/css2?family=Montserrat:wght@400;600;700;800&display=swap" rel="stylesheet">
<style>
  :root {
    --grey-light: #dcdddc;
    --charcoal: #3a3735;
    --maroon-dark: #4a2a2a;
    --maroon: #7c2a2a;
    --red: #c62828;
    --red-bright: #d62f2d;
    --red-muted: #8c2626;
    --white: #ffffff;
  }
  * { margin: 0; padding: 0; box-sizing: border-box; }
  html, body { width: 1200px; height: 375px; overflow: hidden; background: var(--charcoal); }
  .banner {
    position: relative;
    width: 1200px;
    height: 375px;
    overflow: hidden;
    font-family: "Montserrat", Arial, sans-serif;
    background: linear-gradient(90deg, var(--maroon-dark) 0%, var(--maroon-dark) 22%, var(--maroon) 55%, var(--red) 85%, var(--red) 100%);
  }
  .grey-wedge {
    position: absolute; inset: 0;
    background: var(--grey-light);
    clip-path: polygon(0 0, 621px 0, 0 325px);
  }
  .mission-band {
    position: absolute; left: 0; top: 268px;
    width: 1200px; height: 107px;
    background: var(--charcoal);
  }
  .port-scene {
    position: absolute; inset: 0;
    background: linear-gradient(160deg, var(--red-bright) 0%, var(--red) 45%, #5a2626 100%);
    clip-path: polygon(1200px 90px, 1200px 375px, 840px 375px, 860px 300px, 960px 150px, 1110px 96px);
  }
  .brand {
    position: absolute; left: 40px; top: 110px;
    display: flex; align-items: center; gap: 12px;
  }
  .brand-dot {
    width: 18px; height: 18px; border-radius: 50%;
    background: var(--red);
  }
  .brand-name {
    font-weight: 800; font-size: 40px; letter-spacing: 1px;
    color: var(--red); line-height: 1;
  }
  .values { list-style: none; }
  .value {
    position: absolute;
    font-size: 24px; font-weight: 400; color: var(--white);
    white-space: nowrap; line-height: 1; text-align: right;
  }
  .value strong { font-weight: 700; }
  .core-title {
    position: absolute; left: 637px; top: 188px;
    font-weight: 800; font-size: 38px; line-height: 0.9;
    letter-spacing: 3px; color: var(--red-bright);
  }
  .core-title span { display: block; }
  .core-title .second { margin-left: 52px; }
  .mission-title {
    position: absolute; left: 118px; top: 281px;
    font-weight: 800; font-size: 31px; letter-spacing: 4px;
    color: var(--red-muted); line-height: 1;
  }
  .mission-text {
    position: absolute; left: 0; top: 315px; width: 842px;
    text-align: center; color: var(--white);
    font-size: 18.5px; font-weight: 400; line-height: 25px;
  }
</style>
</head>
<body>
  <div class="banner">
    <div class="grey-wedge"></div>
    <div class="mission-band"></div>
    <div class="port-scene" role="img" aria-label="Illustration of a container ship, crane and shipping containers at port"></div>

    <div class="brand">
      <span class="brand-dot"></span>
      <span class="brand-name">TEK Logistics</span>
    </div>

    <ul class="values">
      <li class="value" style="right:21px; top:50px;">DO THE <strong>RIGHT THINGS</strong> FOR THE <strong>RIGHT REASONS</strong></li>
      <li class="value" style="right:212px; top:86px;">PURSUE <strong>GROWTH</strong> AND <strong>DEVELOPMENT</strong></li>
      <li class="value" style="right:279px; top:121px;">BUILD A <strong>POSITIVE TEAM ATMOSPHERE</strong></li>
      <li class="value" style="right:402px; top:157px;">DELIVER <strong>WOW</strong> THROUGH <strong>SERVICE</strong></li>
      <li class="value" style="right:596px; top:193px;">DO EVERYTHING <strong>SAFELY</strong></li>
      <li class="value" style="right:832px; top:229px;">HAVE <strong>FUN</strong></li>
    </ul>

    <h2 class="core-title"><span>CORE</span><span class="second">VALUES</span></h2>

    <h2 class="mission-title">MISSION</h2>
    <p class="mission-text">Provide the best customer experience while creating an environment of<br>growth and opportunity for our customers, employees, and service providers.</p>
  </div>
</body>
</html>
```